Distribution company for alcoholic beverages called Amber Ledger needs a web design

1. We would like to first page to show

A. The company logo (in att)

B. A wall of bottles similar to
- www.tallcaskhollow.com that will click through to the brand info
- https://velmarcellars.com/brands/
PLEASE NOTE THAT IT CAN NOT BE THE SAME DESIGN - it needs to have a different look and feel ... this is to show what we mean with a wall of bottles

Important = we need to be able to keep adding new bottles/brands over time

C. only 3 tabs needed – Brands, About Us and Contact

Style
- simple and clean
- colourful
- classy

2. Page 2
The intro page to describe the company
we can use the same (Box + drop) logo to create a visual

3. Page 3
The referral page to the specific brands/company
= we need to alternating versions of this / just different ordering in the page

Target Market(s)

importers, brand owners, bartenders,

Industry/Entity Type

It Company

Number of Pages Required

3 page

Requirements
Must have
• A landing page visual that can display bottles we will sell in an organised way
• We need to be able to add bottles when the portfolio expands
Nice to have
• to have the drop out of the logo as a part of the design of the website

```html
<!DOCTYPE html>
<html lang="en">
<head>
<meta charset="utf-8">
<title>Amber Ledger — About Us</title>
<link href="https://fonts.googleapis.com/css2?family=Herr+Von+Muellerhoff&family=Montserrat:wght@700&display=swap" rel="stylesheet">
<style>
  :root {
    --ink: #000000;
    --paper: #ffffff;
    --flame-light: #f7b733;
    --flame-mid: #d9660f;
    --cask-brown: #5a1e06;
    --cask-dark: #1c0602;
    --ghost-frame: #f1f1f1;
  }
  * { margin: 0; padding: 0; box-sizing: border-box; }
  html, body {
    width: 1200px; height: 812px; overflow: hidden;
    background: var(--paper);
  }
  .page {
    position: relative; width: 1200px; height: 812px;
    font-family: Arial, Helvetica, sans-serif;
  }
  .site-header {
    position: absolute; left: 0; top: 0; width: 1200px; height: 73px;
    background: var(--ink);
  }
  .brand-mark {
    position: absolute; left: 96px; top: 17px; width: 150px; height: 40px;
    border: 2px solid var(--paper);
    display: flex; align-items: center; justify-content: center;
    color: var(--paper);
    font-family: 'Montserrat', Arial, sans-serif; font-weight: 700;
    font-size: 14px; letter-spacing: 1px; text-decoration: none;
  }
  .main-nav a {
    position: absolute; top: 18px;
    font-family: 'Herr Von Muellerhoff', cursive;
    font-size: 28px; color: var(--paper); text-decoration: none;
    white-space: nowrap;
  }
  .nav-about { left: 786px; }
  .nav-brands { left: 925px; }
  .nav-contact { left: 1050px; }

  .hero-photo {
    position: absolute; left: 0; top: 73px; width: 605px; height: 666px;
    background:
      radial-gradient(ellipse 90% 45% at 50% 10%, var(--flame-light) 0%, var(--flame-mid) 45%, transparent 80%),
      linear-gradient(180deg, var(--flame-mid) 0%, var(--cask-brown) 50%, var(--cask-dark) 100%);
  }
  .hero-frame {
    position: absolute; left: 143px; top: 260px; width: 299px; height: 298px;
    border: 3px solid var(--paper);
  }
  .hero-title {
    position: absolute; left: 143px; top: 360px; width: 299px;
    text-align: center; color: var(--paper);
    font-family: 'Herr Von Muellerhoff', cursive; font-size: 84px; line-height: 1;
    white-space: nowrap;
  }

  .intro {
    position: absolute; left: 605px; top: 73px; width: 595px; height: 666px;
    background: var(--paper);
  }
  .intro-backdrop {
    position: absolute; left: 209px; top: 174px; width: 176px; height: 171px;
    border: 6px solid var(--ghost-frame);
  }
  .intro-heading {
    position: absolute; left: 0; top: 255px; width: 600px;
    text-align: center; font-family: 'Herr Von Muellerhoff', cursive;
    font-weight: 400; font-size: 72px; line-height: 1; color: var(--ink);
  }
  .intro-copy {
    position: absolute; left: 119px; top: 364px; width: 362px;
    text-align: center; font-size: 12px; line-height: 16.7px; color: var(--ink);
  }
  .intro-copy p + p { margin-top: 16.7px; }

  .site-footer {
    position: absolute; left: 0; top: 739px; width: 1200px; height: 73px;
    background: var(--ink); color: var(--paper);
  }
  .copyright {
    position: absolute; left: 95px; top: 29px; font-size: 12px;
  }
  .copyright a { color: var(--paper); }
  .social-link {
    position: absolute; top: 28px; width: 18px; height: 18px;
    border-radius: 50%; background: var(--paper);
  }
  .social-one { left: 1047px; }
  .social-two { left: 1084px; }
</style>
</head>
<body>
<div class="page">
  <header class="site-header">
    <a class="brand-mark" href="#">AMBER LEDGER</a>
    <nav class="main-nav">
      <a class="nav-about" href="#">About Us</a>
      <a class="nav-brands" href="#">Brands</a>
      <a class="nav-contact" href="#">Contact</a>
    </nav>
  </header>

  <section class="hero-photo" role="img" aria-label="Photograph of oak barrels with flames rising from their open tops in a dark cellar">
    <div class="hero-frame"></div>
    <h1 class="hero-title">About Us</h1>
  </section>

  <section class="intro">
    <div class="intro-backdrop" aria-hidden="true"></div>
    <h2 class="intro-heading">Amber Ledger</h2>
    <div class="intro-copy">
      <p>Lorem ipsum dolor sit amet, consectetur adipiscing elit, sed do eiusmod tempor incididunt ut labore et dolore magna aliqua. Ut enim ad minim veniam, quis nostrud exercitation ullamco laboris nisi ut aliquip ex ea commodo consequat.</p>
      <p>Duis aute irure dolor in reprehenderit in voluptate velit esse cillum dolore eu fugiat nulla pariatur. Excepteur sint occaecat cupidatat non proident, sunt in culpa qui officia deserunt mollit anim id est laborum.</p>
    </div>
  </section>

  <footer class="site-footer">
    <p class="copyright">Copyright © 2018 Amber Ledger. <a href="#">Terms &amp; Conditions </a></p>
    <a class="social-link social-one" href="#" aria-label="Social profile"></a>
    <a class="social-link social-two" href="#" aria-label="Social profile"></a>
  </footer>
</div>
</body>
</html>
```